The book is called Amber Lantern. Subtitle is ‘Morning finds us all.’

Books is based on the day Jesus did 3 things happened. The curtain in the temple tore in two, a great earthquake and many of the holy saints rose from the dead. It never says in the bible what happened to them. The book is based on that those ‘holy one” are still here today meeting people in there time of need.

```html
<!DOCTYPE html>
<html lang="en">
<head>
<meta charset="utf-8">
<title>Amber Lantern — Cover</title>
<link rel="stylesheet" href="https://fonts.googleapis.com/css2?family=Cinzel:wght@400;500&display=swap">
<style>
  :root {
    --slate-deep: #050505;
    --slate-mid: #141414;
    --slate-soft: #1c1c1c;
    --gold-light: #cf9d3c;
    --gold-deep: #9a6630;
    --gold-rule: #a8772f;
  }
  html, body {
    margin: 0;
    padding: 0;
    width: 848px;
    height: 1200px;
    overflow: hidden;
    background: var(--slate-deep);
  }
  .cover {
    position: relative;
    width: 848px;
    height: 1200px;
    overflow: hidden;
  }
  .cover__stone {
    position: absolute;
    inset: 0;
    background:
      radial-gradient(ellipse 60% 45% at 55% 35%, var(--slate-soft) 0%, transparent 70%),
      radial-gradient(ellipse 50% 40% at 30% 75%, var(--slate-mid) 0%, transparent 70%),
      linear-gradient(160deg, var(--slate-mid) 0%, var(--slate-deep) 60%, #0a0a0a 100%);
  }
  .cover__title {
    position: absolute;
    inset: 0;
    width: 848px;
    height: 1200px;
  }
  .title-word {
    font-family: "Cinzel", serif;
    font-weight: 400;
  }
  .subtitle {
    font-family: "Cinzel", serif;
    font-weight: 400;
    fill: var(--gold-rule);
  }
  .title-rule {
    stroke: var(--gold-rule);
    stroke-width: 2;
  }
</style>
</head>
<body>
  <main class="cover">
    <div class="cover__stone" role="img" aria-label="Dark slate stone texture background"></div>

    <svg class="cover__title" viewBox="0 0 848 1200" xmlns="http://www.w3.org/2000/svg">
      <defs>
        <linearGradient id="gold-fill" x1="0" y1="0" x2="0" y2="1">
          <stop offset="0" stop-color="var(--gold-light)"/>
          <stop offset="1" stop-color="var(--gold-deep)"/>
        </linearGradient>
      </defs>

      <text class="title-word" x="118" y="526" font-size="172"
            textLength="614" lengthAdjust="spacingAndGlyphs"
            fill="url(#gold-fill)">AMBER</text>

      <text class="title-word" x="124" y="697" font-size="126"
            textLength="599" lengthAdjust="spacingAndGlyphs"
            fill="url(#gold-fill)">LANTERN</text>

      <line class="title-rule" x1="122" y1="724" x2="715" y2="724"/>

      <text class="subtitle" x="125" y="785" font-size="40"
            textLength="602" lengthAdjust="spacingAndGlyphs">MORNING FINDS US ALL.</text>
    </svg>
  </main>
</body>
</html>
```